Dentistry Office

We want a new design for a Dentist's office website.

The theme is: "We provide high quality, state-of-the-art, dental care in a comfortable, caring environment."

The site currently has a menu on the left of the page with about 40 items on it. There is a great deal of textual content on each page, plus several illustrations.

We want to do this using CSS, so we need specifications in the CSS for all possible elements. The CSS needs to be named in a logical manner for easy use.

Every dentist on the planet seems to use lots of Flash. We don't want to because it is so distracting. We are looking for an elegant solution targeting 24-55 age group, but not excluding anyone.

The following (from another dentist's site) can give you a taste of what we want to communicate on the site:

"After 20 years of teaching dentists how to refine their technique and many years of writing textbooks, I currently devote my time to my office and the hands-on practice of dentistry. I'd like to welcome you personally to my dental practice, and I invite you to meet my highly experienced team of professionals.

"We have offered complete dental care of the highest quality since 1978. We provide Preventive Services, Tooth Whitening and Cosmetic Dentistry for a beautiful smile, Endodontics (root canal treatment) to treat painful teeth, Sedation Dentistry so you can relax, and Dental Implants to restore what is missing. We offer total care.

"Our approach to your health is simple: We use our education, experience and dedication to provide every patient with superior dental care.

"This passion for excellence is not just a goal, but a standard every member of our team holds.

"We also pride ourselves with our state of the art procedures, training and technology. This includes creating a beautiful smile using techniques that preserve as much of the original tooth as possible.

"Our abilities are renowned throughout the dental profession and I hope if you have any questions you will contact us by an e-mail note, by phone or just by dropping by."

Keep in mind the screen shape and dimensions. Your design needs to work in the normal screen proportions, regardless of how it looks when you post it here. Scrolling is OK, but the first impression needs to work.

Keep in mind that there will be about 250 words, or more, on each page.

Competitors web sites:

http://www.brellwickdentist.example/

http://www.brellwickdentalcare.example/

http://www.grinsbybrellwickdental.example/

http://www.dorvanfamilydentalcare.example/

http://www.brellwickdental.example/

http://www.quimbertdental.example/

We need to compete with these.

Target Market(s)

Generally adults seeking the most experienced and comfortable-to-be-with dentist.

Industry/Entity Type

Training

Requirements
Must have
• Must stand apart from other dentists.
• Must be elegant.
• Must have a horizontal menu structure across all columns, NOT a vertical that requires scrolling, no popout, pop down, etc. menus.
• We are looking for something special.
• Do not waste your time or ours putting up templates and things you have used before.
• Personally, I do not see how someone outside the US can understand the northern California dental market. But you are welcome to try.
Should not have
• Flash or graphics that move
• The look of a template
• Folksy fonts
• Looks like you used it 20 times before

```html
<!DOCTYPE html>
<html lang="en">
<head>
<meta charset="utf-8">
<title>Dentist's Office</title>
<link href="https://fonts.googleapis.com/css2?family=Arimo:wght@400;700&family=Open+Sans:wght@400;600&display=swap" rel="stylesheet">
<style>
:root{
  --navy:#0f4b6c;
  --sky:#3aa6d8;
  --page:#ffffff;
  --row:#e6e6e6;
  --row-line:#ffffff;
  --text:#5a5a5a;
  --ink:#222222;
  --heading:#1b5f86;
  --heading-soft:#8a8a8a;
  --accent:#e79a2c;
  --tab-active:#e8e8e8;
}
*{box-sizing:border-box;margin:0;padding:0}
html,body{width:892px;height:1200px;overflow:hidden}
body{background:var(--navy);font-family:"Arimo",Arial,sans-serif;position:relative}
.page{position:absolute;left:18px;top:22px;width:855px;height:1141px;background:var(--page)}
.brand{position:absolute;left:52px;top:40px;display:flex;align-items:center;gap:10px}
.brand-dot{width:36px;height:36px;border-radius:50%;background:var(--sky)}
.brand-name{font-size:21px;font-weight:700;color:var(--navy)}
.call{position:absolute;right:32px;top:32px;font-size:17px;font-weight:700;color:var(--navy)}
.call span{color:#8c8c8c}
.main-nav{position:absolute;left:10px;top:92px;width:836px;height:41px;background:var(--navy);border-radius:4px;display:flex;align-items:center}
.main-nav a{color:#fff;text-decoration:none;font-size:17.5px;height:41px;line-height:41px;padding:0 13px}
.main-nav a:first-child{padding-left:16px}
.main-nav a.active{background:var(--tab-active);color:var(--ink);margin:0 12px 0 10px;padding:0 7px}
.hero{position:absolute;left:8px;top:138px;width:840px;height:231px;border-radius:8px;overflow:hidden;border:1px solid #ddd}
.hero-photo{position:absolute;inset:0;background:linear-gradient(90deg,#c9b39c 0%,#e7dcd2 28%,#f6f4f2 42%,#f6f4f2 56%,#d8c5b3 70%,#e9d3b5 100%)}
.hero-kicker{position:absolute;left:225px;top:12px;font-size:15.5px;color:var(--accent);font-family:"Open Sans",sans-serif}
.hero-title{position:absolute;left:276px;top:34px;font-size:19px;color:#444;font-family:"Open Sans",sans-serif}
.hero-tag{position:absolute;left:0;bottom:0;width:178px;height:35px;background:var(--navy);color:#fff;font-family:"Open Sans",sans-serif;font-size:17.5px;line-height:35px;padding-left:4px;border-top-right-radius:6px}
.topic-menu{position:absolute;left:10px;top:377px;width:650px;height:143px;display:flex;gap:5px}
.topic-group{flex:0 0 auto}
.topic-group.education{width:128px}
.topic-group.preventative{width:140px}
.topic-group.cosmetics{width:127px}
.topic-group.restorations{width:125px}
.topic-group.visiting{width:110px}
.topic-group h3{background:var(--navy);color:#fff;font-weight:400;font-size:12.5px;text-align:center;height:17px;line-height:17px;white-space:nowrap}
.topic-group ul{list-style:none}
.topic-group li{background:var(--row);border-bottom:1px solid var(--row-line);font-size:10px;color:var(--ink);height:14px;line-height:13px;padding-left:6px;white-space:nowrap}
.quick-contact{position:absolute;left:669px;top:377px;width:177px;height:143px;background:var(--navy);border-radius:8px;color:#fff;font-size:10.5px}
.quick-contact h4{font-weight:400;font-size:13.5px;text-align:center;padding-top:10px}
.quick-contact .phone{position:absolute;left:12px;top:42px}
.quick-contact .lines{position:absolute;left:89px;top:44px;line-height:17px}
.quick-contact .foot{position:absolute;left:6px;top:94px;line-height:17px}
.content{position:absolute;left:10px;top:528px;width:836px;height:597px;background:#fff;border-radius:18px;box-shadow:0 1px 6px rgba(0,0,0,.25);padding:18px 20px 0 20px}
.content h1{font-family:"Open Sans",sans-serif;font-weight:600;font-size:24px;color:var(--heading);margin-bottom:8px;line-height:34px}
.content h1 span{font-weight:400;color:var(--heading-soft);font-size:29px}
.content p{font-family:"Open Sans",sans-serif;font-size:11.3px;color:var(--text);letter-spacing:.25px;line-height:18px;margin-bottom:6px}
.site-footer{position:absolute;left:0;top:1163px;width:892px;height:37px;color:#fff;font-size:11px;line-height:37px}
.site-footer .copy{position:absolute;left:36px}
.site-footer nav{position:absolute;right:38px}
.site-footer nav a{color:#fff;text-decoration:none}
.site-footer nav i{font-style:normal;padding:0 5px}
</style>
</head>
<body>
<div class="page">
  <div class="brand"><span class="brand-dot"></span><span class="brand-name">Dentist's Office</span></div>
  <div class="call">Call us: <span>000-000-0000</span></div>

  <nav class="main-nav">
    <a href="#">Home</a><a href="#">Why we are Different</a><a href="#" class="active">Technologies we offer</a><a href="#">Meet Doctors</a><a href="#">Our Team</a><a href="#">Contact Us</a>
  </nav>

  <section class="hero">
    <div class="hero-photo" role="img" aria-label="Smiling family and two smiling young women"></div>
    <div class="hero-kicker">Do you want a better looking Smile?</div>
    <div class="hero-title">Visit our Office</div>
    <div class="hero-tag">Looking better smile</div>
  </section>

  <nav class="topic-menu">
    <div class="topic-group education"><h3>Education</h3><ul>
      <li>Emergency Dental Care</li><li>Your Mouth</li><li>Your Tooth</li><li>Cracked Tooth?</li><li>Missing a Tooth?</li><li>Sensitive Teeth</li><li>Dry Mouth</li><li>Tooth Grinding</li><li>Sleep Dentistry</li></ul></div>
    <div class="topic-group preventative"><h3>Preventative</h3><ul>
      <li>What is Preventative Care?</li><li>Taking Care of Your Teeth</li><li>Eating Right</li><li>Dental Check-Ups</li><li>Sealants</li><li>Periodontal Disease</li><li>Kicking the Habit</li><li>Night Gurards</li></ul></div>
    <div class="topic-group cosmetics"><h3>Cosmetics</h3><ul>
      <li>Cosmetic Dentistry</li><li>Bleaching and Whitening</li><li>Cosmetic Bonding</li><li>Esthetic Veneers</li><li>Tooth Shaping</li></ul></div>
    <div class="topic-group restorations"><h3>Restorations</h3><ul>
      <li>Crowns/Caps:Each Step</li><li>CMBRs</li><li>Porcelain Bridges</li><li>Bonded Dental Bridges</li><li>Gold Restorations</li><li>Implants</li></ul></div>
    <div class="topic-group visiting"><h3>Visiting our office</h3><ul>
      <li>Where to Stay</li><li>First Visit / Map</li><li>Financial Policy</li><li>Dental Insurance</li></ul></div>
  </nav>

  <div class="quick-contact">
    <h4>Our Quick Contact</h4>
    <svg class="phone" width="60" height="42" viewBox="0 0 60 42" aria-hidden="true">
      <rect x="14" y="14" width="42" height="24" rx="4" fill="#2a2a2a"/>
      <rect x="4" y="4" width="10" height="34" rx="4" fill="#1a1a1a"/>
      <rect x="24" y="19" width="22" height="5" fill="#9fb7c6"/>
      <g fill="#777"><rect x="24" y="27" width="4" height="3"/><rect x="31" y="27" width="4" height="3"/><rect x="38" y="27" width="4" height="3"/><rect x="24" y="32" width="4" height="3"/><rect x="31" y="32" width="4" height="3"/><rect x="38" y="32" width="4" height="3"/></g>
    </svg>
    <div class="lines">Sample text<br>Sample text</div>
    <div class="foot">Sample text here Sample text here<br>Sample text here Sample text here</div>
  </div>

  <main class="content">
    <h1>Welcome to <span>Dentist office</span></h1>
    <p>After 20 years of teaching dentists how to refine their technique and many years of writing textbooks, I currently devote my time to my office and the hands-on practice of dentistry. to welcome you personally to my dental practice, and I invite you to meet my highly experienced team of professionals.</p>
    <p>We have offered complete dental care of the highest quality since 1978. We provide Preventive Services, Tooth Whitening and Cosmetic Dentistry for a beautiful smile,Endodontics (root canal treatment) to treat painful teeth, Sedation Dentistry so you can relax,and Dental Implants to restore what is missing.</p>
    <p>We offer total care.</p>
    <p>Our approach to your health is simple: We use our education, experience and dedication to provide every patient with superior dental care.</p>
    <p>This passion for excellence is not just a goal, but a standard every member of our team holds.</p>
    <p>We also pride ourselves with our state of the art procedures, training and technology. This includes creating a beautiful smile using techniques that preserve as much of the original tooth as possible.</p>
    <p>Our abilities are renowned throughout the dental profession and I hope if you have any questions you will contact us by an e-mail note, by phone or just by dropping by.</p>
    <p>We also pride ourselves with our state of the art procedures, training and technology. This includes creating a beautiful smile using techniques that preserve as much of the original tooth as possible.</p>
    <p>We also pride ourselves with our state of the art procedures, training and technology. This includes creating a beautiful smile using techniques that preserve as much of the original tooth as possible.</p>
    <p>We also pride ourselves with our state of the art procedures, training and technology. This includes creating a beautiful smile using techniques that preserve as much of the original tooth as possible.</p>
    <p>Our abilities are renowned throughout the dental profession and I hope if you have any questions you will contact us by an e-mail note, by phone or just by dropping by.</p>
    <p>We also pride ourselves with our state of the art procedures, training and technology. This includes creating a beautiful smile using techniques that preserve as much of the original tooth as possible.</p>
  </main>
</div>

<footer class="site-footer">
  <span class="copy">copyright 2010 Dentist office All rights reserved.</span>
  <nav><a href="#">Home</a><i>|</i><a href="#">Why we are Different</a><i>|</i><a href="#">Technologies we offer</a><i>|</i><a href="#">Meet Doctors</a><i>|</i><a href="#">Out Team</a><i>|</i><a href="#">Contact us</a></nav>
</footer>
</body>
</html>
```